Business Card Design

Our Motto is "Protecting Australia's Underground Utilities"

We want the Southern Cross inside a shield I have attached the southern cross and our old shield design

Product description is: Vacuum Excavation & Utility Location
Wet & Dry Vacuum Loading
Confined Space Entry Specialists
High Pressure Cleaning

The Southern Cross in the shield must be blue and white. The Company name must be Coastal Pipeguard Services. The Green & Gold Shield logo I uploaded is my OLD logo design. Thank you

Target Market(s)

Civil Construction

Industry/Entity Type

Business

Contact Information for Business Card

Coastal Pipeguard Services Pty Ltd
Corey Halbrook(Director)
0413862975
coreyh@pipeguardco.com.au
A.B.N.52938470116

Colors
0456a3

Requirements
Must have
• Southern Cross inside a shield, Blue and white design on the Southern Cross shield.
Must say Coastal Pipeguard Services P/L

```html
<!DOCTYPE html>
<html lang="en">
<head>
<meta charset="utf-8">
<title>Coastal Pipeguard Services – Business Card</title>
<link rel="stylesheet" href="https://fonts.googleapis.com/css2?family=Arimo:wght@400;700&display=swap">
<style>
  :root {
    --backdrop: #bdbdbd;
    --card: #ffffff;
    --brand-blue: #0456a3;
    --title-blue: #2a5ea8;
    --rule-blue: #8fb0d8;
    --flag-blue: #2a3590;
    --flag-blue-light: #3a47a6;
    --ink: #1a1a1a;
    --muted: #555555;
    --logo-green: #1d7a3a;
  }
  * { box-sizing: border-box; margin: 0; padding: 0; }
  html, body { width: 1200px; height: 960px; overflow: hidden; }
  body {
    background: var(--backdrop);
    font-family: "Arimo", Arial, sans-serif;
    position: relative;
  }
  .card {
    position: absolute;
    width: 600px;
    height: 350px;
    background: var(--card);
    border-radius: 26px;
    box-shadow: 0 6px 18px rgba(0,0,0,0.18);
    overflow: hidden;
  }
  .card--front { left: 90px; top: 90px; }
  .card--back { left: 510px; top: 520px; }

  .rule {
    position: absolute;
    height: 1px;
    background: linear-gradient(90deg, rgba(143,176,216,0) 0%, var(--rule-blue) 25%, var(--rule-blue) 75%, rgba(143,176,216,0) 100%);
  }

  /* brand mark stand-in */
  .brand-mark {
    display: flex; flex-direction: column; align-items: center; gap: 8px;
  }
  .brand-mark__dot {
    width: 56px; height: 56px; border-radius: 50%;
    background: var(--logo-green);
  }
  .brand-mark__name {
    font-weight: 700; font-size: 20px; color: var(--logo-green);
    letter-spacing: 1px; text-transform: uppercase;
  }

  /* front */
  .card--front .brand-mark {
    position: absolute; left: 0; right: 0; top: 58px;
  }
  .front-title {
    position: absolute; left: 0; right: 0; top: 178px;
    text-align: center;
    font-variant: small-caps; font-size: 15px; color: var(--title-blue);
    letter-spacing: 0.4px;
  }
  .front-title__line { top: 198px; left: 30px; right: 30px; }
  .flag {
    position: absolute; left: 250px; top: 204px;
    width: 100px; height: 68px;
    background: linear-gradient(135deg, var(--flag-blue-light), var(--flag-blue));
  }
  .front-base__line { top: 280px; left: 20px; right: 20px; }
  .motto {
    position: absolute; left: 0; right: 0; top: 296px;
    text-align: center;
    font-size: 12px; font-style: normal; color: var(--muted);
    letter-spacing: 0.6px;
  }

  /* back */
  .back-brand {
    position: absolute; right: 60px; top: 30px;
    display: flex; flex-direction: column; align-items: flex-end; gap: 8px;
  }
  .back-brand .brand-mark { align-items: center; gap: 4px; }
  .back-brand .brand-mark__dot { width: 30px; height: 30px; }
  .back-brand .brand-mark__name { font-size: 11px; }
  .back-company {
    font-variant: small-caps; font-size: 13px; color: var(--title-blue);
    letter-spacing: 0.3px;
  }
  .back-top__line { top: 124px; left: 60px; right: 0; }
  .person {
    position: absolute; right: 60px; top: 136px; text-align: right;
  }
  .person__name { font-variant: small-caps; font-size: 13px; color: var(--ink); }
  .person__role { font-size: 12px; color: var(--brand-blue); }
  .services {
    position: absolute; left: 34px; top: 146px;
    list-style: none;
    font-size: 11px; line-height: 18px; color: var(--muted);
  }
  .contacts {
    position: absolute; right: 40px; top: 200px;
    list-style: none; display: flex; flex-direction: column; gap: 8px;
    align-items: flex-end;
  }
  .contacts__item {
    display: flex; align-items: center; gap: 8px;
    font-size: 13px; color: var(--ink); letter-spacing: 0.3px;
  }
  .contacts__icon { width: 16px; height: 16px; fill: var(--ink); }
  .back-base__line { top: 300px; left: 0; right: 60px; }
</style>
</head>
<body>

  <section class="card card--front" aria-label="Card front">
    <div class="brand-mark">
      <span class="brand-mark__dot"></span>
      <span class="brand-mark__name">Pipeguard</span>
    </div>
    <p class="front-title">Coastal Pipeguard Services</p>
    <div class="rule front-title__line"></div>
    <div class="flag" role="img" aria-label="Southern Cross flag, white stars on blue"></div>
    <div class="rule front-base__line"></div>
    <p class="motto">Protecting Australia's Underground Utilities</p>
  </section>

  <section class="card card--back" aria-label="Card back">
    <div class="back-brand">
      <div class="brand-mark">
        <span class="brand-mark__dot"></span>
        <span class="brand-mark__name">Pipeguard</span>
      </div>
      <p class="back-company">Coastal Pipeguard Services Pty Ltd</p>
    </div>
    <div class="rule back-top__line"></div>
    <div class="person">
      <p class="person__name">Corey Halbrook</p>
      <p class="person__role">Director</p>
    </div>
    <ul class="services">
      <li>Vacuum Excavation &amp; Utility Location</li>
      <li>Wet &amp; Dry Vacuum Loading</li>
      <li>Confined Space Entry Specialists</li>
      <li>High Pressure Cleaning</li>
    </ul>
    <ul class="contacts">
      <li class="contacts__item">0413862975
        <svg class="contacts__icon" viewBox="0 0 16 16" aria-hidden="true"><path d="M2 5c0-2 2-3 6-3s6 1 6 3v1h-3V5H5v1H2z"/><rect x="3" y="7" width="10" height="7" rx="1"/></svg>
      </li>
      <li class="contacts__item">coreyh@pipeguardco.com.au
        <svg class="contacts__icon" viewBox="0 0 16 16" aria-hidden="true"><path d="M1 3h14v10H1z M2 4l6 5 6-5" fill="none" stroke="#1a1a1a" stroke-width="1.4"/></svg>
      </li>
      <li class="contacts__item">A.B.N.52938470116
        <svg class="contacts__icon" viewBox="0 0 16 16" aria-hidden="true"><path d="M8 1a5 5 0 0 0-5 5c0 4 5 9 5 9s5-5 5-9a5 5 0 0 0-5-5zm0 7a2 2 0 1 1 0-4 2 2 0 0 1 0 4z"/></svg>
      </li>
    </ul>
    <div class="rule back-base__line"></div>
  </section>

</body>
</html>
```